We sell companies excess stock for them

We need a business card for a company based in New Zealand called 'StockHarbor'.

Check out our website to get an idea www.stockharbor.example

We help other businesses to;
- Sell Excess Stock
- Manage Product Returns
- Sell Company Assets

Our logo is attached for your reference
The font used is 'RifficFree-Bold'

Target Market(s)

Businesses

Industry/Entity Type

Business

Contact Information for Business Card

Name: Mark Pellow
Phone: 027 846 2093
email: markpellow@stockharbor.example
website: www.stockharbor.example

Font styles to use
Other font styles liked:
• Unsure

Colors
9bcb3b

Requirements
Must have
• coming soon
Nice to have
• coming soon
Should not have
• coming soon

```html
<!DOCTYPE html>
<html lang="en">
<head>
<meta charset="utf-8">
<title>StockHarbor – Mark Pellow</title>
<link rel="stylesheet" href="https://fonts.googleapis.com/css2?family=Big+Shoulders+Display:wght@100&family=Bebas+Neue&family=Josefin+Sans:wght@400;500;700&display=swap">
<style>
  :root {
    --green: #9bcb3b;
    --ink: #0d1321;
    --black: #000000;
    --paper: #ffffff;
  }
  html, body {
    margin: 0;
    padding: 0;
    width: 1200px;
    height: 667px;
    overflow: hidden;
    background: var(--paper);
  }
  .card {
    position: relative;
    width: 1200px;
    height: 667px;
    background: var(--paper);
    overflow: hidden;
  }
  .card__bands {
    position: absolute;
    inset: 0;
    width: 1200px;
    height: 667px;
  }
  .card__bands rect { fill: var(--green); }

  .person-name {
    position: absolute;
    left: 0;
    width: 1290px;
    top: 226px;
    margin: 0;
    text-align: center;
    font-family: "Bebas Neue", "Arial Narrow", sans-serif;
    font-weight: 400;
    font-size: 124px;
    line-height: 1;
    color: var(--black);
    letter-spacing: 1px;
  }
  .company-wordmark {
    position: absolute;
    left: 27px;
    width: 1090px;
    top: 322px;
    margin: 0;
    display: flex;
    justify-content: space-between;
    font-family: "Big Shoulders Display", "Arial Narrow", sans-serif;
    font-weight: 100;
    font-size: 106px;
    line-height: 1;
    color: var(--green);
  }
  .contact {
    position: absolute;
    right: 98px;
    top: 524px;
    display: flex;
    gap: 28px;
    margin: 0;
    font-family: "Josefin Sans", sans-serif;
    font-weight: 400;
    font-size: 24px;
    line-height: 1;
    color: var(--ink);
    white-space: nowrap;
  }
  .contact__email { color: var(--green); }
  .contact__phone { font-weight: 500; }
  .brand {
    position: absolute;
    left: 45px;
    top: 596px;
    margin: 0;
    font-family: "Josefin Sans", sans-serif;
    font-weight: 700;
    font-size: 37px;
    line-height: 1;
    color: var(--black);
    letter-spacing: -0.5px;
  }
  .social {
    position: absolute;
    left: 1102px;
    top: 36px;
    display: flex;
    flex-direction: column;
    gap: 12px;
  }
  .social__dot {
    width: 40px;
    height: 40px;
    border: 2px solid var(--black);
    border-radius: 50%;
    box-sizing: border-box;
  }
  .hashtag {
    position: absolute;
    left: 1122px;
    top: 212px;
    margin: 0;
    transform: translate(-50%, -50%) rotate(-90deg);
    font-family: "Josefin Sans", sans-serif;
    font-weight: 400;
    font-size: 16px;
    line-height: 1;
    color: var(--black);
    white-space: nowrap;
  }
</style>
</head>
<body>
  <main class="card">
    <svg class="card__bands" viewBox="0 0 1200 667" aria-hidden="true">
      <rect x="0" y="0" width="520" height="18"/>
      <rect x="0" y="0" width="14" height="220"/>
      <rect x="1186" y="150" width="14" height="140"/>
      <rect x="620" y="649" width="580" height="18"/>
    </svg>

    <h1 class="person-name">Mark Pellow</h1>

    <p class="company-wordmark" aria-label="StockHarbor">
      <span>S</span><span>T</span><span>O</span><span>C</span><span>K</span><span>H</span><span>A</span><span>R</span><span>B</span><span>O</span><span>R</span>
    </p>

    <p class="contact">
      <span class="contact__web">stockharbor.example</span>
      <span class="contact__email">markpellow@stockharbor.example</span>
      <span class="contact__phone">027 846 2093</span>
    </p>

    <p class="brand">StockHarbor</p>

    <div class="social" aria-hidden="true">
      <span class="social__dot"></span>
      <span class="social__dot"></span>
    </div>

    <p class="hashtag">#stockharbor</p>
  </main>
</body>
</html>
```